biopharma company with breakthrough technology needs new web design

The rise of multidrug resistant bacteria pose a worldwide healthcare crisis as new bacterial strains are now resistant to nearly all existing antibiotics. Q4 Biolabs is developing a class of new compounds known as ceragenins that have broad spectrum activity against even resistant strains. Our website needs a facelift. See www.q4biolabs.example. We want to provide more information on the landing page and make it more visually appealing. see for example: http://vornatrix.example/#sthash.KbwRtmPe.xqzt
Industry/Entity Type
Healthcare

```html
<!DOCTYPE html>
<html lang="en">
<head>
<meta charset="utf-8">
<title>Q4 Biolabs</title>
<link href="https://fonts.googleapis.com/css2?family=Open+Sans:wght@300;400;600;700&family=Raleway:wght@400;600;700&display=swap" rel="stylesheet">
<style>
:root{
  --cyan:#1fb6ee;
  --cyan-dark:#0f9bd1;
  --navy:#1d3f78;
  --ink:#333a40;
  --muted:#8a9096;
  --line:#e3e6e8;
  --soft:#f4f5f6;
  --footer:#2b2f33;
  --footer-deep:#222528;
  --white:#ffffff;
}
*{box-sizing:border-box;margin:0;padding:0}
html,body{width:1200px;height:2756px;overflow:hidden}
body{font-family:"Open Sans",Arial,sans-serif;color:var(--ink);background:var(--white);font-size:13px;line-height:1.6}
a{color:inherit;text-decoration:none}
.btn{display:inline-block;border:1px solid currentColor;padding:7px 18px;font-size:10px;font-weight:600;letter-spacing:1px;text-transform:uppercase}
.btn-solid{background:var(--cyan);color:var(--white);border-color:var(--cyan)}

/* header */
.site-header{height:70px;position:relative;border-bottom:1px solid var(--line)}
.brand{position:absolute;left:60px;top:14px;display:flex;align-items:center;gap:8px}
.brand-dot{width:34px;height:34px;border-radius:50%;background:var(--navy)}
.brand-name{font-family:"Raleway",sans-serif;font-weight:700;font-size:22px;color:var(--navy)}
.topbar{position:absolute;right:60px;top:0;background:var(--cyan);color:var(--white);font-size:11px;padding:3px 14px;display:flex;gap:8px;align-items:center}
.topbar strong{font-weight:700}
.main-nav{position:absolute;right:60px;top:38px;display:flex;gap:0}
.main-nav a{font-size:10px;font-weight:600;letter-spacing:.5px;text-transform:uppercase;padding:6px 16px;color:var(--ink)}
.main-nav a.active{color:var(--cyan);border-bottom:2px solid var(--cyan)}

/* hero */
.hero{height:750px;position:relative;background:radial-gradient(circle at 30% 40%,#cfe5ec 0%,#9fc2cc 45%,#5f8d98 100%);text-align:center;color:var(--white)}
.hero-art{position:absolute;inset:0}
.hero-copy{position:absolute;left:0;right:0;top:235px}
.hero-copy h1{font-family:"Raleway",sans-serif;font-weight:600;font-size:26px;line-height:1.3}
.hero-copy p{font-family:"Raleway",sans-serif;font-size:24px;margin-top:4px}
.hero-copy .btn{margin-top:22px}

/* intro */
.intro{height:210px;text-align:center;padding-top:38px}
.intro h2{font-family:"Raleway",sans-serif;font-weight:600;font-size:24px;color:var(--ink)}
.intro .lead{font-size:15px;color:var(--muted);font-weight:300}
.intro .body{width:700px;margin:8px auto 0;font-size:10px;color:var(--muted);line-height:1.5}
.intro .btn{margin-top:16px;color:var(--muted)}

/* feature rows */
.feature{display:flex;height:215px}
.feature.alt{height:225px;background:var(--soft)}
.feature-media{width:600px;height:100%}
.feature-text{width:600px;padding:30px 60px 0 44px}
.feature.alt .feature-text{padding:34px 40px 0 60px}
.feature-text h3{font-family:"Raleway",sans-serif;font-weight:600;font-size:20px;margin-bottom:10px}
.feature-text p{font-size:10px;color:var(--muted);line-height:1.55;margin-bottom:8px}
.feature-text .btn{color:var(--muted);margin-top:4px}

/* clients and news */
.voices{height:310px;display:flex;padding:30px 60px 0}
.testimonial{width:520px;padding-right:40px}
.news{flex:1;border-left:1px solid var(--line);padding-left:30px}
.block-title{font-family:"Raleway",sans-serif;font-weight:600;font-size:18px;border-bottom:1px solid var(--line);padding-bottom:6px;position:relative}
.block-title .more{position:absolute;right:0;bottom:8px;font-family:"Open Sans",sans-serif;font-size:10px;color:var(--cyan);font-weight:400;text-decoration:underline}
.quote-card{margin-top:24px;position:relative;padding:10px 0 0 60px}
.quote-mark{position:absolute;left:0;top:0;font-family:Georgia,serif;font-size:70px;line-height:1;color:#c9cdd1}
.quote-card p{font-size:11px;color:var(--muted);font-style:italic;line-height:1.55}
.quote-author{margin-top:28px;display:flex;align-items:center;gap:16px;background:var(--soft);padding:10px 14px 10px 60px}
.quote-author .who{flex:1;text-align:center}
.quote-author .who strong{display:block;font-size:11px}
.quote-author .who span{font-size:9px;color:var(--muted)}
.avatar{width:60px;height:60px;border-radius:50%;background:linear-gradient(135deg,#b89a86,#4c5a68)}
.news-item{display:flex;gap:16px;margin-top:22px}
.news-date{width:42px;height:46px;background:var(--cyan);color:var(--white);text-align:center;font-size:15px;font-weight:700;line-height:1.1;padding-top:6px}
.news-date small{display:block;font-size:8px;font-weight:400}
.news-body strong{font-size:11px;display:block}
.news-body p{font-size:10px;color:var(--muted);line-height:1.45}
.news-body a{font-size:9px;color:var(--ink);font-weight:600}

/* team */
.team{height:420px;background:var(--cyan);position:relative;color:var(--white);text-align:center;padding-top:26px}
.team h2{font-family:"Raleway",sans-serif;font-weight:600;font-size:22px}
.team-rule{width:60px;height:1px;background:rgba(255,255,255,.6);margin:8px auto 0}
.team-grid{display:flex;justify-content:center;gap:60px;margin-top:40px}
.member{width:190px}
.member svg{display:block;margin:0 auto}
.member strong{display:block;font-size:12px;font-weight:600;margin-top:14px}
.member span{font-size:9px;opacity:.9}
.arrow{position:absolute;top:194px;width:30px;height:30px;border-radius:50%;background:rgba(255,255,255,.25);display:flex;align-items:center;justify-content:center}
.arrow.left{left:50px}.arrow.right{right:50px}

/* call to action */
.cta{height:210px;text-align:center;padding-top:50px}
.cta h2{font-family:"Raleway",sans-serif;font-weight:600;font-size:20px;color:var(--cyan-dark)}
.cta p{font-size:13px;color:var(--muted);font-weight:300}
.cta .btn{margin-top:20px;color:var(--ink);font-size:9px}

/* footer */
.site-footer{height:346px;background:var(--footer);color:#b7bcc1;position:relative}
.footer-cols{display:flex;padding:42px 60px 0}
.footer-col{width:360px}
.footer-col h4{font-size:9px;font-weight:700;letter-spacing:1px;text-transform:uppercase;color:#d7dadd;margin-bottom:10px}
.footer-col p,.footer-col li{font-size:9px;line-height:1.7}
.footer-col ul{list-style:none}
.footer-col li::before{content:"› ";color:var(--cyan)}
.footer-col li.active{color:var(--cyan)}
.signup{display:flex;margin:10px 0 26px}
.signup span{width:180px;height:24px;background:#1f2225;border:1px solid #3b4045;font-size:9px;color:#7b8086;padding:4px 8px}
.signup b{width:24px;height:24px;background:var(--cyan)}
.social{display:flex;gap:10px;margin-top:8px}
.social i{width:14px;height:14px;border-radius:50%;background:var(--cyan);display:block}
.footer-bottom{position:absolute;left:0;right:0;bottom:0;height:40px;background:var(--footer-deep);font-size:9px;color:#7b8086;padding:13px 60px}
.to-top{position:absolute;right:60px;top:10px;width:20px;height:20px;border:1px solid #4a5056;border-radius:50%}
</style>
</head>
<body>

<header class="site-header">
  <a class="brand" href="#"><span class="brand-dot"></span><span class="brand-name">Q4 Biolabs</span></a>
  <div class="topbar">
    <svg width="10" height="10" viewBox="0 0 24 24" aria-hidden="true"><path fill="#fff" d="M6.6 10.8a15 15 0 0 0 6.6 6.6l2.2-2.2c.3-.3.7-.4 1-.2 1.1.4 2.3.6 3.6.6.6 0 1 .4 1 1V20c0 .6-.4 1-1 1A17 17 0 0 1 3 4c0-.6.4-1 1-1h3.5c.6 0 1 .4 1 1 0 1.3.2 2.5.6 3.6.1.3 0 .7-.2 1z"/></svg>
    <span>Call Us Now:</span><strong>800-555-0148</strong>
  </div>
  <nav class="main-nav">
    <a class="active" href="#">Home</a><a href="#">About</a><a href="#">Technology</a><a href="#">Medical Devices</a><a href="#">News</a><a href="#">Contact</a>
  </nav>
</header>

<section class="hero">
  <div class="hero-art" role="img" aria-label="Microscopic view of bacteria and virus particles in pale teal tones"></div>
  <div class="hero-copy">
    <h1>Fortifying Medical Devices With Their Own Immune Systems</h1>
    <p>To Prevent Hospital-Acquired Infections</p>
    <a class="btn btn-solid" href="#">Learn More</a>
  </div>
</section>

<section class="intro">
  <h2>Q4 Biolabs is a development-stage medical device company</h2>
  <p class="lead">commercializing antimicrobial medical devices and coatings</p>
  <p class="body">Q4 Biolabs is a development-stage medical device company focused on commercializing antimicrobial medical devices and coatings to address the worldwide threat of multidrug resistant bacteria and prevent device-associated and hospital-acquired infections across clinical care.</p>
  <a class="btn" href="#">Discover More</a>
</section>

<section class="feature">
  <div class="feature-media" role="img" aria-label="Laboratory test tubes and glassware in blue and orange light" style="background:linear-gradient(120deg,#f2a93b 0%,#f6d28a 30%,#9fd3e8 60%,#2b8fc8 100%)"></div>
  <div class="feature-text">
    <h3>Ceragenin Technology</h3>
    <p>Ceragenins, also known as cationic steroidal antimicrobials or CSAs, are synthetic small molecule mimics of endogenous antimicrobial peptides found in the innate immune system.</p>
    <p>Ceragenins have broad spectrum activity, including strains of drug resistant bacteria, fungi and viruses, and resist the development of resistance.</p>
    <a class="btn" href="#">Learn More</a>
  </div>
</section>

<section class="feature alt">
  <div class="feature-text">
    <h3>Medical Devices</h3>
    <p>• Q4 Biolabs has been focused on antimicrobial device coatings. There is a critical need for devices that resist colonization and biofilm formation in patients.</p>
    <p>• The Q4 coated endotracheal tube is our initial device, built to reduce ventilator-associated pneumonia in critically ill patients requiring intubation.</p>
    <p>• Ceragenin coatings show sustained activity against bacteria that form biofilms on catheters, implants and orthopedic hardware.</p>
  </div>
  <div class="feature-media" role="img" aria-label="Molecular model with blue and white spheres in a laboratory setting" style="background:linear-gradient(135deg,#eef4f8 0%,#bcd6e8 50%,#3f7fb8 100%)"></div>
</section>

<section class="voices">
  <div class="testimonial">
    <div class="block-title">What Our Clients Say</div>
    <div class="quote-card">
      <span class="quote-mark">“</span>
      <p>Lorem ipsum dolor sit amet, consectetur adipiscing elit, sed do eiusmod tempor incididunt ut labore et dolore magna aliqua. Ut enim ad minim veniam, quis nostrud exercitation ullamco laboris nisi ut aliquip ex ea commodo consequat.</p>
    </div>
    <div class="quote-author">
      <div class="who"><strong>Mr. Adrian Pell</strong><span>CEO of Larkfield Health Inc.</span></div>
      <div class="avatar" role="img" aria-label="Portrait of the client"></div>
    </div>
  </div>
  <div class="news">
    <div class="block-title">Latest News <a class="more" href="#">View all News</a></div>
    <div class="news-item">
      <div class="news-date">28<small>JUNE</small></div>
      <div class="news-body">
        <strong>Q4 Biolabs To Join Panel</strong>
        <p>Q4 Biolabs, an emerging pharmaceutical company addressing the increasing global health challenges through the development of new antimicrobial device technology.</p>
        <a href="#">Read More »</a>
      </div>
    </div>
    <div class="news-item">
      <div class="news-date">29<small>JUNE</small></div>
      <div class="news-body">
        <strong>Q4 Study Data Presented at Conference</strong>
        <p>Q4 Biolabs, an emerging pharmaceutical company addressing the increasing global health challenges through the development of new antimicrobial device technology.</p>
        <a href="#">Read More »</a>
      </div>
    </div>
  </div>
</section>

<section class="team">
  <h2>Meet Our Team</h2>
  <div class="team-rule"></div>
  <a class="arrow left" href="#"><svg width="10" height="10" viewBox="0 0 10 10"><path d="M7 1 3 5l4 4" stroke="#fff" stroke-width="1.6" fill="none"/></svg></a>
  <a class="arrow right" href="#"><svg width="10" height="10" viewBox="0 0 10 10"><path d="M3 1l4 4-4 4" stroke="#fff" stroke-width="1.6" fill="none"/></svg></a>
  <div class="team-grid">
    <div class="member">
      <svg width="170" height="170" viewBox="0 0 170 170" role="img" aria-label="Portrait of Marcus Olden"><polygon points="85,4 155,44 155,126 85,166 15,126 15,44" fill="#fff"/><polygon points="85,10 150,47 150,123 85,160 20,123 20,47" fill="#c9b6a6"/></svg>
      <strong>Marcus Olden</strong><span>Chief Executive Officer</span>
    </div>
    <div class="member">
      <svg width="170" height="170" viewBox="0 0 170 170" role="img" aria-label="Portrait of Peter Halvorsen"><polygon points="85,4 155,44 155,126 85,166 15,126 15,44" fill="#fff"/><polygon points="85,10 150,47 150,123 85,160 20,123 20,47" fill="#5a4a42"/></svg>
      <strong>Peter Halvorsen</strong><span>President and Chief Operating Officer</span>
    </div>
    <div class="member">
      <svg width="170" height="170" viewBox="0 0 170 170" role="img" aria-label="Portrait of Daniel R. Kessler"><polygon points="85,4 155,44 155,126 85,166 15,126 15,44" fill="#fff"/><polygon points="85,10 150,47 150,123 85,160 20,123 20,47" fill="#b9876a"/></svg>
      <strong>Daniel R. Kessler</strong><span>Chief Financial Officer</span>
    </div>
    <div class="member">
      <svg width="170" height="170" viewBox="0 0 170 170" role="img" aria-label="Portrait of Thomas J. Avery"><polygon points="85,4 155,44 155,126 85,166 15,126 15,44" fill="#fff"/><polygon points="85,10 150,47 150,123 85,160 20,123 20,47" fill="#7d8a96"/></svg>
      <strong>Thomas J. Avery</strong><span>Executive Chairman</span>
    </div>
  </div>
</section>

<section class="cta">
  <h2>Let's make something great together</h2>
  <p>Get in touch with us and send some basic info for a quick quote</p>
  <a class="btn" href="#">Contact Us</a>
</section>

<footer class="site-footer">
  <div class="footer-cols">
    <div class="footer-col">
      <h4>Stay Connected</h4>
      <p>Subscribe to our newsletter for updates</p>
      <div class="signup"><span>Enter Email Address</span><b></b></div>
      <h4>Get Social</h4>
      <div class="social"><i></i><i></i><i></i></div>
    </div>
    <div class="footer-col">
      <h4>Navigate</h4>
      <ul>
        <li class="active">Home</li><li>About</li><li>Technology</li><li>Medical Devices</li><li>News</li><li>Contact</li>
      </ul>
    </div>
    <div class="footer-col">
      <h4>Keep in Touch</h4>
      <p>Q4 Biolabs<br>214 Harbor Lane<br>Riverton, OH 45001</p>
      <p style="margin-top:10px">Contact Us:<br>800-555-0148</p>
    </div>
  </div>
  <div class="footer-bottom">© 2016 Q4 Biolabs. All rights reserved.<span class="to-top"></span></div>
</footer>

</body>
</html>
```